Business Card Design for Photographer

Updating business card design. Must use included logo. We're a luxury wedding photography business. Elegancy, luxury, consistency are messages we wish to convey.

Visit our website at www.colbyvarnway.com to familiarize yourself more with our brand design currently (fonts, colors etc.). This is what we want to maintain.

Target Market(s)

Luxury Brides and Grooms

Industry/Entity Type

Wedding

Contact Information for Business Card

Current logo (attached to brief)
Name: Colby Varnway
Phone: 5208813047
website/blog
Email

Requirements
Must have
• Current logo (attached to brief)
• Name: Colby Varnway
• Phone: 5208813047
• website/blog
• Email
• Instagram username
Should not have
• bright colors, fonts that don't suit our brand (visit www.colbyvarnway.com)

```html
<!DOCTYPE html>
<html lang="en">
<head>
<meta charset="utf-8">
<title>Colby Varnway Photographers – Business Card</title>
<link rel="stylesheet" href="https://fonts.googleapis.com/css2?family=Marcellus&family=Open+Sans:wght@400;600&display=swap">
<style>
  :root {
    --bg: #ece9e4;
    --card: #ffffff;
    --ink: #111111;
    --logo-grey: #5f5f5f;
    --rule: #9a9a9a;
    --photo-green-dark: #2f3e2a;
    --photo-green: #5e7250;
    --photo-light: #e8e8e6;
    --band: rgba(255, 255, 255, 0.62);
  }
  * { box-sizing: border-box; margin: 0; padding: 0; }
  html, body { width: 1200px; height: 1200px; overflow: hidden; }
  body {
    background: var(--bg);
    font-family: "Open Sans", sans-serif;
    color: var(--ink);
    position: relative;
  }
  .card {
    position: absolute;
    left: 150px;
    width: 900px;
    height: 514px;
    background: var(--card);
    box-shadow: 0 6px 18px rgba(0, 0, 0, 0.18);
    overflow: hidden;
  }
  .card--front { top: 62px; }
  .card--back { top: 624px; }

  .front-photo {
    position: absolute;
    inset: 0;
    background:
      linear-gradient(180deg, transparent 78%, var(--photo-light) 92%),
      radial-gradient(ellipse at 72% 55%, #f4f4f2 0 22%, transparent 40%),
      linear-gradient(90deg, var(--photo-green-dark) 0%, var(--photo-green) 35%, #7c8a6c 55%, var(--photo-green-dark) 100%);
  }
  .front-band {
    position: absolute;
    left: 0; right: 0;
    top: 200px;
    height: 160px;
    background: var(--band);
    display: flex;
    align-items: center;
    justify-content: center;
  }

  .brand {
    display: flex;
    align-items: center;
    gap: 16px;
    font-family: "Marcellus", serif;
    text-transform: uppercase;
    letter-spacing: 0.16em;
    font-weight: 400;
  }
  .brand__mark { width: 36px; height: 36px; flex: none; }
  .brand--front { color: var(--ink); font-size: 26px; }
  .brand--front .brand__mark { background: var(--ink); }
  .brand--back { color: var(--logo-grey); font-size: 30px; }
  .brand--back .brand__mark { background: var(--logo-grey); width: 44px; height: 44px; }

  .back-header {
    position: absolute;
    top: 96px; left: 0; right: 0;
    display: flex;
    flex-direction: column;
    align-items: center;
  }
  .back-rule {
    margin-top: 26px;
    width: 300px;
    height: 1px;
    background: var(--rule);
  }
  .back-details {
    position: absolute;
    top: 290px; left: 0; right: 0;
    display: flex;
    justify-content: center;
    align-items: center;
  }
  .holder-name {
    font-size: 26px;
    font-weight: 600;
    width: 300px;
    text-align: right;
    padding-right: 34px;
  }
  .divider {
    width: 2px;
    height: 118px;
    background: #555;
  }
  .contact-list {
    list-style: none;
    padding-left: 30px;
    width: 360px;
    font-size: 19px;
    font-weight: 600;
    line-height: 1.45;
  }
  .contact-list li { display: flex; align-items: center; gap: 10px; }
  .contact-list svg { width: 15px; height: 15px; flex: none; fill: none; stroke: var(--ink); stroke-width: 2; }
</style>
</head>
<body>

<section class="card card--front" aria-label="Business card front">
  <div class="front-photo" role="img" aria-label="Wedding photograph: bride and groom embracing beside a white vintage car in a flowering garden"></div>
  <div class="front-band">
    <div class="brand brand--front">
      <span class="brand__mark"></span>
      <span class="brand__name">Colby Varnway Photographers</span>
    </div>
  </div>
</section>

<section class="card card--back" aria-label="Business card back">
  <header class="back-header">
    <div class="brand brand--back">
      <span class="brand__mark"></span>
      <span class="brand__name">Colby Varnway Photographers</span>
    </div>
    <div class="back-rule"></div>
  </header>

  <div class="back-details">
    <p class="holder-name">Colby Varnway</p>
    <div class="divider"></div>
    <ul class="contact-list">
      <li>
        <svg viewBox="0 0 16 16" aria-hidden="true"><path d="M4 1.5l2.5 3-1.5 1.8c.8 1.8 2.3 3.3 4.2 4.2L11 9l3 2.5-1.6 2.8C7 14 2 9 1.7 3.2z"/></svg>
        5208813047
      </li>
      <li>
        <svg viewBox="0 0 16 16" aria-hidden="true"><rect x="1.5" y="3.5" width="13" height="9"/><path d="M1.5 3.5L8 9l6.5-5.5"/></svg>
        colby@colbyvarnway.com
      </li>
      <li>
        <svg viewBox="0 0 16 16" aria-hidden="true"><circle cx="8" cy="8" r="6.5"/><path d="M1.5 8h13M8 1.5c-3 3.5-3 9.5 0 13M8 1.5c3 3.5 3 9.5 0 13"/></svg>
        www.colbyvarnway.com
      </li>
    </ul>
  </div>
</section>

</body>
</html>
```